Zielgruppe
Wir vermieten Köche und Küchenhilfen an unsere Kunden. Die Visitenkarten sind sowohl für potentielle Neukunden als auch potentielle neue Mitarbeitern.
Aufgabenstellung
Unsere Visitenkarten sollen modern sein ohne zu voll zu wirken.
Auf ihr enthalten sollen sein: Logo, Name, Position, Telefonnr (Festnetz und Mobil), Adresse, Email und Logo.
Ein kurzer, knapper Motivationsspruch wäre auch schön.

```html
<!DOCTYPE html>
<html lang="de">
<head>
<meta charset="utf-8">
<title>Tarvo Catering – Visitenkarten</title>
<link rel="stylesheet" href="https://fonts.googleapis.com/css2?family=Fira+Sans:ital,wght@0,400;0,500;1,400&family=Fira+Sans+Condensed:wght@500;600&display=swap">
<style>
  :root {
    --board: #2b2b2b;
    --board-dark: #1c1c1c;
    --card: #ffffff;
    --ink: #4a4a4a;
    --ink-dark: #333333;
    --orange: #e8641a;
    --band-grey: #6f6f6f;
    --band-dark: #444444;
  }
  * { margin: 0; padding: 0; box-sizing: border-box; }
  html, body { width: 1200px; height: 2579px; overflow: hidden; }
  body {
    position: relative;
    background: radial-gradient(ellipse at 50% 40%, var(--board) 0%, var(--board-dark) 100%);
    font-family: "Fira Sans", sans-serif;
    color: var(--ink);
  }
  .card {
    position: absolute;
    width: 485px;
    height: 749px;
    background: var(--card);
    overflow: hidden;
  }
  .col-left { left: 70px; }
  .col-right { left: 638px; }
  .row-1 { top: 72px; }
  .row-2 { top: 892px; }
  .row-3 { top: 1728px; }

  .band {
    position: absolute;
    left: 0;
    width: 100%;
  }
  .band-top {
    top: 0;
    background: linear-gradient(180deg, var(--band-dark) 0%, var(--band-grey) 60%, var(--orange) 100%);
  }
  .band-bottom {
    bottom: 0;
    background: linear-gradient(0deg, var(--band-dark) 0%, var(--band-grey) 60%, var(--orange) 100%);
  }

  .brand {
    position: absolute;
    left: 0; right: 0;
    display: flex;
    align-items: center;
    justify-content: center;
    gap: 14px;
    font-weight: 500;
    color: var(--ink);
    white-space: nowrap;
  }
  .brand-dot { border-radius: 50%; background: var(--orange); flex: none; }
  .brand-lg { font-size: 40px; }
  .brand-lg .brand-dot { width: 60px; height: 60px; }
  .brand-sm { font-size: 28px; gap: 10px; }
  .brand-sm .brand-dot { width: 40px; height: 40px; }
  .brand-corner { left: auto; right: 55px; justify-content: flex-end; font-size: 24px; gap: 10px; }
  .brand-corner .brand-dot { width: 36px; height: 36px; }

  .center { position: absolute; left: 0; right: 0; text-align: center; white-space: nowrap; }
  .quote-caps {
    font-variant: small-caps;
    font-size: 24px;
    line-height: 30px;
    letter-spacing: 1px;
    color: var(--ink-dark);
  }
  .quote-author { color: var(--orange); font-variant: small-caps; font-size: 17px; letter-spacing: 0.5px; }
  .web {
    font-family: "Fira Sans Condensed", sans-serif;
    font-weight: 500;
    font-size: 22px;
    letter-spacing: 1px;
    color: var(--orange);
  }
  .web-light {
    position: absolute;
    left: 94px;
    color: #ffffff;
    font-size: 15px;
    letter-spacing: 0.5px;
  }

  .contact-caps { font-variant: small-caps; letter-spacing: 1px; color: var(--ink-dark); }
  .person-caps { font-family: "Fira Sans Condensed", sans-serif; font-weight: 600; font-size: 34px; }
  .role-caps { font-size: 19px; }
  .address-caps { font-size: 20px; line-height: 27px; }
  .phone { color: var(--orange); font-size: 20px; line-height: 27px; letter-spacing: 0.8px; }
  .phone .contact-caps { color: var(--orange); }
  .mail-caps { font-size: 17px; }

  .quote-right {
    position: absolute;
    right: 78px;
    text-align: right;
    font-style: italic;
    font-size: 24px;
    line-height: 30px;
    color: var(--ink-dark);
  }
  .quote-right .quote-author { font-style: normal; font-variant: normal; font-size: 17px; }

  .line-left { position: absolute; left: 58px; color: var(--ink-dark); white-space: nowrap; }
  .person { font-family: "Fira Sans Condensed", sans-serif; font-weight: 600; font-size: 35px; }
  .role { font-size: 20px; }
  .address { font-size: 20px; line-height: 27px; }
  .line-left.phone { color: var(--orange); letter-spacing: 0.3px; }
  .mail { font-size: 20px; }
  .tagline {
    font-family: "Fira Sans Condensed", sans-serif;
    font-weight: 600; font-size: 22px; color: var(--orange);
  }
</style>
</head>
<body>

  <section class="card col-left row-1">
    <div class="brand brand-lg" style="top:240px"><span class="brand-dot"></span>Tarvo Catering</div>
    <div class="center quote-caps" style="top:414px">“Wege entstehen dadurch,<br>dass man sie geht.”</div>
    <div class="center quote-author" style="top:480px">– Klara Wendt</div>
    <div class="center web" style="top:683px">WWW.TARVO-CATERING.DE</div>
  </section>

  <section class="card col-right row-1">
    <div class="brand brand-lg" style="top:240px"><span class="brand-dot"></span>Tarvo Catering</div>
    <div class="center quote-caps" style="top:414px">“Wege entstehen dadurch,<br>dass man sie geht.”</div>
    <div class="center quote-author" style="top:480px">– Klara Wendt</div>
    <div class="center web" style="top:683px">WWW.TARVO-CATERING.DE</div>
  </section>

  <section class="card col-left row-2">
    <div class="band band-top" style="height:176px" role="img" aria-label="Dekoratives Band in Grau und Orange"></div>
    <div class="brand brand-lg" style="top:390px"><span class="brand-dot"></span>Tarvo Catering</div>
    <div class="center web" style="top:663px">WWW.TARVO-CATERING.DE</div>
  </section>

  <section class="card col-right row-2">
    <div class="brand brand-sm" style="top:66px"><span class="brand-dot"></span>Tarvo Catering</div>
    <div class="center contact-caps person-caps" style="top:232px">Vorname Nachname</div>
    <div class="center contact-caps role-caps" style="top:277px">Geschäftsführer</div>
    <div class="center contact-caps address-caps" style="top:336px">Lindenhof-Strasse 8<br>61130 Nidderau</div>
    <div class="center phone" style="top:414px"><span class="contact-caps">Festnetz:</span> 0175 / 4820193<br><span class="contact-caps">Mobile:</span>&nbsp;&nbsp;&nbsp; 0175 / 4820193</div>
    <div class="center contact-caps mail-caps" style="top:498px">info@tarvo-catering.de</div>
    <div class="band band-bottom" style="height:182px" role="img" aria-label="Dekoratives Band in Grau und Orange"></div>
    <div class="web-light" style="top:683px">WWW.TARVO-CATERING.DE</div>
  </section>

  <section class="card col-left row-3">
    <div class="brand brand-lg" style="top:190px"><span class="brand-dot"></span>Tarvo Catering</div>
    <div class="quote-right" style="top:350px">“Wege entstehen dadurch,<br>dass man sie geht.”<br><span class="quote-author">– Klara Wendt</span></div>
    <div class="band band-bottom" style="height:182px" role="img" aria-label="Dekoratives Band in Grau und Orange"></div>
    <div class="web-light" style="top:680px; font-size:17px; letter-spacing:0">www.tarvo-catering.de</div>
  </section>

  <section class="card col-right row-3">
    <div class="band band-top" style="height:160px" role="img" aria-label="Dekoratives Band in Grau und Orange"></div>
    <div class="brand brand-corner" style="top:190px"><span class="brand-dot"></span>Tarvo Catering</div>
    <div class="line-left person" style="top:315px">Vorname Nachname</div>
    <div class="line-left role" style="top:364px">Geschäftsführer</div>
    <div class="line-left address" style="top:422px">Lindenhof-Straße 8<br>61130 Nidderau</div>
    <div class="line-left phone" style="top:500px">Festnetz: 0175 / 4820193<br>Mobile:&nbsp;&nbsp;&nbsp; 0175 / 4820193</div>
    <div class="line-left mail" style="top:581px">info@tarvo-catering.de</div>
    <div class="line-left tagline" style="top:681px">Event – Personal – Ihr Spezialist</div>
  </section>

</body>
</html>
```